New Email Marketing Design Project

We need an email signature to highlight our brand, as well as include our product ranges. The brand has an Italian origin and we have a logo developed already.
For the email signature please include the following content:
Dane Orrick | Partner
Email: Dane.orrick@velastro.com.au
Office: + 61 2 9584 1726
Mobile: + 61 438 917 254
Web: www.velastro.com.au

Velastro Lifestyle Centre:
Level 2, Brackenridge Design Centre
482 Penrose Street, Waterloo
NSW 2017 Australia

[Product ranges] Kitchen Appliances | Designer Joineries | Blinds & Curtains | Fire Places | Featured Lightings | Smart Home | Bathroom Products

```html
<!DOCTYPE html>
<html lang="en">
<head>
<meta charset="utf-8">
<title>Velastro Email Signature</title>
<link rel="stylesheet" href="https://fonts.googleapis.com/css2?family=Arimo:wght@400;700&display=swap">
<style>
  :root {
    --backdrop: #eeeeee;
    --card: #ffffff;
    --ink: #111111;
    --text: #2a2a2a;
    --accent: #c8102e;
    --rule: #222222;
    --photo-area: #9c9c9c;
  }
  * { margin: 0; padding: 0; box-sizing: border-box; }
  html, body {
    width: 1200px; height: 499px; overflow: hidden;
    background: var(--backdrop);
    font-family: "Arimo", Arial, sans-serif;
    color: var(--text);
  }
  .signature {
    position: absolute; left: 118px; top: 118px;
    width: 965px; height: 263px;
    background: var(--card);
    overflow: hidden;
  }
  .brand {
    position: absolute; left: 23px; top: 82px;
    font-weight: 700; font-size: 42px; letter-spacing: -0.5px;
    color: var(--ink); line-height: 1;
  }
  .person {
    position: absolute; left: 268px; top: 67px;
    font-size: 19px; font-weight: 700; color: var(--ink);
  }
  .person .role { font-size: 13px; font-weight: 400; }
  .contacts {
    position: absolute; left: 268px; top: 100px;
    list-style: none; font-size: 12.5px; line-height: 20.5px;
  }
  .contacts li { display: flex; align-items: center; gap: 6px; white-space: nowrap; }
  .contacts svg { width: 15px; height: 15px; flex: none; }
  .address {
    position: absolute; left: 474px; top: 100px;
    font-size: 12.5px; line-height: 20.5px; font-style: normal;
    white-space: nowrap;
  }
  .address strong { color: var(--text); }
  .divider {
    position: absolute; left: 20px; top: 223px;
    width: 648px; height: 1px; background: var(--rule);
  }
  .ranges {
    position: absolute; left: 23px; top: 232px;
    font-size: 10.6px; color: var(--ink); white-space: nowrap;
  }
  .ranges span + span::before { content: "•"; margin: 0 6px; }
  .showroom {
    position: absolute; left: 690px; top: 0;
    width: 274px; height: 263px;
  }
</style>
</head>
<body>
  <div class="signature">
    <div class="brand">Velastro</div>

    <div class="person">Dane Orrick <span class="role">/ Partner</span></div>

    <ul class="contacts">
      <li>
        <svg viewBox="0 0 16 16"><circle cx="8" cy="8" r="7" fill="none" stroke="var(--accent)" stroke-width="1.4"/><rect x="4.2" y="5.3" width="7.6" height="5.4" fill="var(--accent)"/><path d="M4.2 5.3 L8 8.4 L11.8 5.3" fill="none" stroke="#fff" stroke-width="0.9"/></svg>
        Dane.orrick@velastro.com.au
      </li>
      <li>
        <svg viewBox="0 0 16 16"><circle cx="8" cy="8" r="7" fill="none" stroke="var(--accent)" stroke-width="1.4"/><path d="M5.2 4.4 L6.6 4.2 L7.3 6.2 L6.4 7 Q7.2 8.8 9 9.6 L9.8 8.7 L11.8 9.4 L11.6 10.8 Q8.6 11.6 6.3 9.6 Q4.4 7.6 5.2 4.4 Z" fill="var(--accent)"/></svg>
        +61 2 9584 1726
      </li>
      <li>
        <svg viewBox="0 0 16 16"><circle cx="8" cy="8" r="7" fill="none" stroke="var(--accent)" stroke-width="1.4"/><rect x="5.5" y="3.8" width="5" height="8.4" rx="0.8" fill="none" stroke="var(--accent)" stroke-width="1.2"/><circle cx="8" cy="10.6" r="0.6" fill="var(--accent)"/></svg>
        +61 438 917 254
      </li>
      <li>
        <svg viewBox="0 0 16 16"><circle cx="8" cy="8" r="7" fill="none" stroke="var(--accent)" stroke-width="1.4"/><circle cx="8" cy="8" r="4" fill="var(--accent)"/><path d="M4 8 H12 M8 4 V12 M5.3 5.8 H10.7 M5.3 10.2 H10.7" stroke="#fff" stroke-width="0.6"/></svg>
        www.velastro.com.au
      </li>
    </ul>

    <address class="address">
      <strong>Velastro Lifestyle Centre</strong><br>
      Level 2, Brackenridge Design Centre<br>
      482 Penrose Street, Waterloo<br>
      NSW 2017 Australia
    </address>

    <div class="divider"></div>

    <p class="ranges"><span>Kitchen Appliances</span><span>Designer Joineries</span><span>Blinds &amp; Curtains</span><span>Decor &amp; Accessories</span><span>Lightings</span><span>Smart Home</span><span>Bathroom Products</span></p>

    <svg class="showroom" viewBox="0 0 274 263" role="img" aria-label="Hexagon collage of photographs of a modern kitchen showroom">
      <g fill="var(--photo-area)">
        <polygon points="0,60 27,0 83,0 110,60 83,120 27,120"/>
        <polygon points="0,185 27,125 83,125 110,185 83,245 27,245"/>
        <polygon points="105,0 140,-60 210,-60 245,0 210,60 140,60"/>
        <polygon points="105,125 140,65 210,65 245,125 210,185 140,185"/>
        <polygon points="105,250 140,190 210,190 245,250 210,310 140,310"/>
        <polygon points="240,60 262,0 308,0 335,60 308,120 262,120"/>
        <polygon points="240,185 262,125 308,125 335,185 308,245 262,245"/>
      </g>
    </svg>
  </div>
</body>
</html>
```